Brightwater Spectral Inquiry Website

We are a paranormal research group located in Central Mississippi. We are a group dedicated to help the community in any paranormal investigation. We use fresh new techniques with cutting edge technology to investigate any paranormal situation. Our services are always free of charge to anyone. An unique feature of our group is that we provide a complete history of the property, courtesy of our research team. We would like to see designs that incorporate our logo. We are a professional group and want a professional website.. we will need a home page that will reflect out goals. Links will include "Home, About Us, Contact us, (MAYBE MORE). We will also want a "blank page" with same links that we can edit and fill in all the information..

Target Market(s)

Paranormal-Ghost hunting groups

Industry/Entity Type

Community

Coding

Coded - Design and coding required

Number of Pages Required

2 page

Font styles to use
Other font styles liked:

Requirements
Must have
• we will need a home page that will reflect out goals. Links will include "Home, About Us, Contact us, (MAYBE MORE). We will also want a "blank page" with same links that we can edit and fill in all the information..

```html
<!DOCTYPE html>
<html lang="en">
<head>
<meta charset="utf-8">
<title>Brightwater Spectral Inquiry</title>
<link rel="stylesheet" href="https://fonts.googleapis.com/css2?family=Nova+Round&family=Arimo:wght@400;700&display=swap">
<style>
  :root {
    --yellow: #f2e000;
    --red: #d0181b;
    --text: #8a8a8a;
    --title: #6a6a6a;
    --rule: #e6e6e6;
    --footer: #3f3f3f;
    --icon: #c4c4c4;
    --white: #ffffff;
  }
  * { margin: 0; padding: 0; box-sizing: border-box; }
  html, body { width: 897px; height: 1200px; overflow: hidden; background: var(--white); }
  body { position: relative; font-family: "Arimo", Arial, sans-serif; }
  .hero {
    position: absolute; left: 0; top: 0; width: 897px; height: 486px;
    background:
      linear-gradient(to bottom, rgba(0,0,0,0) 55%, rgba(10,10,10,0.55) 85%, rgba(30,30,30,0.7) 100%),
      linear-gradient(to right, rgba(8,8,8,0.85) 0%, rgba(20,20,20,0.35) 22%, rgba(0,0,0,0) 40%, rgba(0,0,0,0) 62%, rgba(20,20,20,0.35) 80%, rgba(8,8,8,0.8) 100%),
      radial-gradient(ellipse 140px 170px at 480px 290px, #1c1c1c 0%, #2a2a2a 60%, rgba(42,42,42,0) 100%),
      radial-gradient(ellipse 260px 150px at 760px 130px, #9a9a9a 0%, rgba(120,120,120,0) 100%),
      radial-gradient(ellipse 240px 140px at 200px 180px, #8c8c8c 0%, rgba(110,110,110,0) 100%),
      linear-gradient(to bottom, #262626 0%, #5c5c5c 30%, #4a4a4a 60%, #2e2e2e 100%);
  }
  .hero-glow {
    position: absolute; left: 372px; top: 0; width: 150px; height: 140px;
    background: radial-gradient(ellipse at 50% 55%, rgba(255,240,150,0.22) 0%, rgba(255,240,150,0) 70%);
  }
  .nav a {
    position: absolute; top: 55px; color: var(--yellow); text-decoration: none;
    font-size: 12px; letter-spacing: 0.2px;
  }
  .brand {
    position: absolute; left: 392px; top: 48px; width: 110px; height: 32px;
    display: flex; align-items: center; justify-content: center; gap: 6px;
    font-family: "Nova Round", sans-serif; color: var(--yellow); font-size: 22px;
  }
  .brand-dot { width: 10px; height: 10px; border-radius: 50%; background: var(--yellow); }
  .hero-title {
    position: absolute; left: 0; width: 897px; top: 288px; text-align: center;
    font-family: "Nova Round", sans-serif; color: var(--yellow); font-size: 48px; line-height: 60px; font-weight: 400;
  }
  .hero-sub {
    position: absolute; left: 0; width: 897px; top: 356px; text-align: center;
    font-family: "Nova Round", sans-serif; color: var(--white); font-size: 30px; line-height: 34px; letter-spacing: 3px;
  }
  .dots { position: absolute; left: 418px; top: 421px; display: flex; gap: 6px; }
  .dots span { width: 8px; height: 8px; border-radius: 50%; background: var(--red); }
  .dots span.active { background: var(--yellow); }
  .heading {
    position: absolute; font-family: "Nova Round", sans-serif; color: var(--red); font-weight: 400;
    font-size: 19px; text-transform: uppercase; letter-spacing: 0.5px; line-height: 24px;
  }
  .copy { position: absolute; color: var(--text); font-size: 8.6px; line-height: 16px; }
  .welcome-text { left: 99px; width: 430px; letter-spacing: -0.1px; }
  .video {
    position: absolute; left: 542px; top: 535px; width: 256px; height: 152px;
    background: radial-gradient(circle at 50% 50%, #a89a10 0%, #5a1010 50%, #0b0b0b 100%);
  }
  .rule { position: absolute; left: 99px; width: 699px; height: 1px; background: var(--rule); }
  .arrows { position: absolute; left: 768px; top: 734px; display: flex; gap: 1px; }
  .arrows span { width: 15px; height: 14px; background: #8f8f8f; display: flex; align-items: center; justify-content: center; }
  .card { position: absolute; top: 766px; width: 221px; }
  .card-image { width: 221px; height: 132px; box-shadow: 0 3px 3px rgba(0,0,0,0.15); }
  .card-title { margin-top: 18px; color: var(--title); font-weight: 700; font-size: 10.5px; padding-left: 1px; }
  .card-text { margin-top: 8px; color: var(--text); font-size: 8.6px; line-height: 16px; padding-left: 1px; }
  .about-text { left: 178px; width: 540px; top: 1057px; text-align: center; line-height: 17.5px; }
  .footer { position: absolute; left: 0; top: 1147px; width: 897px; height: 53px; background: var(--footer); }
  .footer-copy { position: absolute; left: 99px; top: 22px; color: #d8d8d8; font-size: 8.6px; }
  .social { position: absolute; left: 653px; top: 13px; }
</style>
</head>
<body>
  <header class="hero" role="img" aria-label="Black and white photo of a haunted Victorian mansion between bare twisted trees under a stormy sky">
    <div class="hero-glow"></div>
    <nav class="nav">
      <a href="#" style="left:189px">HOME</a>
      <a href="#" style="left:294px">ABOUT US</a>
      <a href="#" style="left:528px">YOUR STORIES</a>
      <a href="#" style="left:678px">CONTACT US</a>
    </nav>
    <div class="brand"><span class="brand-dot"></span>BSI</div>
    <h1 class="hero-title">BRIGHTWATER</h1>
    <p class="hero-sub">SPECTRAL INQUIRY</p>
    <div class="dots"><span></span><span></span><span class="active"></span><span></span><span></span></div>
  </header>

  <h2 class="heading" style="left:99px; top:503px">Welcome to BSI</h2>
  <p class="copy welcome-text" style="top:539px">Sed ut perspiciatis unde omnis iste natus error sit voluptatem accusantium doloremque laudantium, totam rem aperiam, eaque ipsa quae ab illo inventore veritatis et quasi architecto beatae vitae dicta sunt explicabo. Nemo enim ipsam voluptatem quia voluptas sit aspernatur aut odit aut fugit, sed quia consequuntur magni dolores eos qui ratione voluptatem sequi nesciunt.</p>
  <p class="copy welcome-text" style="top:617px">Sed ut perspiciatis unde omnis iste natus error sit voluptatem accusantium doloremque laudantium, totam rem aperiam, eaque ipsa quae ab illo inventore veritatis et quasi architecto beatae vitae dicta sunt explicabo. Nemo enim ipsam voluptatem quia voluptas sit aspernatur aut odit aut fugit, sed quia consequuntur magni dolores eos qui ratione voluptatem sequi nesciunt.</p>
  <div class="video" role="img" aria-label="Video still of a yellow illustrated hand over a red and black background">
    <svg width="256" height="152" viewBox="0 0 256 152">
      <circle cx="128" cy="76" r="20" fill="rgba(255,255,255,0.15)" stroke="#fff" stroke-width="2"/>
      <path d="M122 66 L138 76 L122 86 Z" fill="#fff"/>
    </svg>
  </div>

  <div class="rule" style="top:711px"></div>

  <h2 class="heading" style="left:98px; top:729px">Your Stories</h2>
  <div class="arrows">
    <span><svg width="6" height="8" viewBox="0 0 6 8"><path d="M5 0 L1 4 L5 8" fill="none" stroke="#fff"/></svg></span>
    <span><svg width="6" height="8" viewBox="0 0 6 8"><path d="M1 0 L5 4 L1 8" fill="none" stroke="#fff"/></svg></span>
  </div>

  <article class="card" style="left:98px">
    <div class="card-image" role="img" aria-label="Photo of a ghostly bride in a white dress inside a ruined room" style="background:linear-gradient(135deg,#2a2a12,#a8a468 50%,#3a3a1c)"></div>
    <h3 class="card-title">INVENTORE VERITATIS</h3>
    <p class="card-text">Sed ut perspiciatis unde omnis iste natus error sit volup-tatem accusantium doloremque laudantium, totam rem beatae vitae dicta sunt explicabo.</p>
  </article>
  <article class="card" style="left:338px">
    <div class="card-image" role="img" aria-label="Blue night-vision photo of a frightened girl in bed" style="background:linear-gradient(135deg,#0e2350,#5a7bb8 55%,#1b3668)"></div>
    <h3 class="card-title">INVENTORE VERITATIS</h3>
    <p class="card-text">Sed ut perspiciatis unde omnis iste natus error sit volup-tatem accusantium doloremque laudantium, totam rem beatae vitae dicta sunt explicabo.</p>
  </article>
  <article class="card" style="left:577px">
    <div class="card-image" role="img" aria-label="Photo of a person thrown across a disordered living room" style="background:linear-gradient(135deg,#3a2c22,#8a6e58 55%,#2c221a)"></div>
    <h3 class="card-title">INVENTORE VERITATIS</h3>
    <p class="card-text">Sed ut perspiciatis unde omnis iste natus error sit volup-tatem accusantium doloremque laudantium, totam rem beatae vitae dicta sunt explicabo.</p>
  </article>

  <div class="rule" style="top:1000px"></div>

  <h2 class="heading" style="left:0; width:897px; text-align:center; top:1023px">About Us</h2>
  <p class="copy about-text">Sed ut perspiciatis unde omnis iste natus error sit voluptatem accusantium doloremque laudantium, totam rem aperiam, eaque ipsa quae ab illo inventore veritatis et quasi architecto beatae vitae dicta sunt explicabo. Nemo enim ipsam voluptatem quia voluptas sit aspernatur aut odit aut fugit, sed quia consequuntur magni dolores eos qui ratione voluptatem sequi nesciunt.</p>

  <footer class="footer">
    <p class="footer-copy">© Copy Rights 2014 BSI.All Rights Reserved.</p>
    <svg class="social" width="150" height="28" viewBox="0 0 150 28" aria-label="Share, email, chat, feed and web links">
      <g fill="none" stroke="var(--icon)" stroke-width="1.2">
        <circle cx="13" cy="14" r="12"/>
        <circle cx="44" cy="14" r="12"/>
        <circle cx="74" cy="14" r="12"/>
        <circle cx="105" cy="14" r="12"/>
        <circle cx="136" cy="14" r="12"/>
        <!-- share -->
        <circle cx="9" cy="14" r="2"/><circle cx="17" cy="9.5" r="2"/><circle cx="17" cy="18.5" r="2"/>
        <path d="M11 13 L15 10.5 M11 15 L15 17.5"/>
        <!-- email -->
        <rect x="37" y="9" width="14" height="10" rx="1"/>
        <path d="M37 10 L44 15 L51 10"/>
        <!-- chat -->
        <path d="M67 9 H81 V17 H73 L69 20 V17 H67 Z"/>
        <!-- feed -->
        <circle cx="100" cy="19" r="1.2" fill="var(--icon)"/>
        <path d="M99 13.5 A6 6 0 0 1 105.5 20 M99 9 A10.5 10.5 0 0 1 110 20"/>
        <!-- web -->
        <circle cx="136" cy="14" r="6.5"/>
        <path d="M129.5 14 H142.5 M136 7.5 C132.5 11 132.5 17 136 20.5 C139.5 17 139.5 11 136 7.5"/>
      </g>
    </svg>
  </footer>
</body>
</html>
```